Ebook cover for a Young Adult adventure novel

We need an ebook cover for our ebook, titled The Hollow Lanterns. You can see the current cover and a description of the book by going to the following link:

http://www.shopveradel.com/Hollow-Lanterns-Vol-1-ebook/dp/Q4R7TX2K9W/ref=sr_1_1?ie=UTF8&qid=1384641616&sr=8-1&keywords=the+hollow+lanterns+vol.+1

Target Market(s)

Young Adults

Industry/Entity Type

Adult

Requirements
Nice to have
• Our main character uses a fencing sword and fights monsters from Vossberg's Hearth Legends. Can you incorporate that?
• We also want our cover to have the same dark "feel" as other Young Adult novels in the fantasy genre.

```html
<!DOCTYPE html>
<html lang="en">
<head>
<meta charset="utf-8">
<title>The Hollow Lanterns – Vol. 1 Cover Spread</title>
<link rel="stylesheet" href="https://fonts.googleapis.com/css2?family=Pinyon+Script&family=Kaushan+Script&display=swap">
<style>
  :root {
    --parchment-light: #d2a45c;
    --parchment-mid: #b07a38;
    --parchment-dark: #5a3412;
    --parchment-edge: #3a200a;
    --spine-shadow: #2c1906;
    --gold: #f3cd4e;
    --gold-deep: #a97a16;
    --frame-gold: #c9a44a;
    --leather: #2b2521;
    --leather-edge: #4a413a;
    --photo-light: #e4e0da;
    --photo-dark: #3a2a22;
  }
  * { margin: 0; padding: 0; box-sizing: border-box; }
  html, body {
    width: 1200px; height: 900px; overflow: hidden;
    background: var(--parchment-edge);
  }
  .spread {
    position: relative; width: 1200px; height: 900px; overflow: hidden;
  }
  .cover {
    position: absolute; top: 0; width: 600px; height: 900px;
    background:
      radial-gradient(ellipse 60% 55% at 50% 50%, rgba(222,178,102,0.55), rgba(222,178,102,0) 70%),
      radial-gradient(ellipse 80% 75% at 50% 50%, var(--parchment-mid) 45%, var(--parchment-dark) 90%, var(--parchment-edge) 100%);
  }
  .cover--back { left: 0; }
  .cover--front { left: 600px; }
  .spine {
    position: absolute; left: 585px; top: 0; width: 30px; height: 900px;
    background: linear-gradient(to right, rgba(44,25,6,0) 0%, rgba(44,25,6,0.75) 45%, var(--spine-shadow) 50%, rgba(44,25,6,0.75) 55%, rgba(44,25,6,0) 100%);
  }
  .corners { position: absolute; inset: 0; }
  .gold-type {
    position: absolute; color: var(--gold);
    text-shadow: 1px 1px 0 var(--gold-deep), 2px 3px 3px rgba(30,15,0,0.7);
    white-space: nowrap;
  }
  .title {
    left: 670px; top: 102px;
    font-family: "Pinyon Script", cursive;
    font-size: 58px; line-height: 1; letter-spacing: 1px;
  }
  .cover-art {
    position: absolute; left: 688px; top: 265px; width: 471px; height: 284px;
    border: 4px solid var(--frame-gold);
    box-shadow: 0 0 0 1px #7a5a1a, 2px 3px 6px rgba(0,0,0,0.5);
    background:
      radial-gradient(ellipse 32% 60% at 56% 70%, var(--photo-dark) 0%, rgba(58,42,34,0.9) 55%, rgba(58,42,34,0) 75%),
      radial-gradient(ellipse 12% 22% at 53% 25%, #4a3328 0%, rgba(74,51,40,0) 100%),
      linear-gradient(135deg, #ece9e4, var(--photo-light));
  }
  .byline {
    font-family: "Kaushan Script", cursive;
    font-size: 25px; letter-spacing: 4px; line-height: 1;
  }
  .byline--first { left: 688px; top: 735px; }
  .byline--amp { left: 688px; top: 785px; }
  .byline--second { left: 688px; top: 842px; }
  .volume {
    right: 38px; top: 846px;
    font-family: "Kaushan Script", cursive;
    font-size: 24px; letter-spacing: 3px; line-height: 1;
  }
</style>
</head>
<body>
<main class="spread">
  <section class="cover cover--back" aria-label="Back cover"></section>
  <section class="cover cover--front" aria-label="Front cover"></section>
  <div class="spine"></div>

  <svg class="corners" width="1200" height="900" viewBox="0 0 1200 900" aria-hidden="true">
    <polygon points="1040,0 1200,0 1200,160" fill="var(--leather)"/>
    <line x1="1040" y1="0" x2="1200" y2="160" stroke="var(--leather-edge)" stroke-width="3"/>
    <polygon points="1040,900 1200,760 1200,900" fill="var(--leather)"/>
    <line x1="1040" y1="900" x2="1200" y2="760" stroke="var(--leather-edge)" stroke-width="3"/>
  </svg>

  <h1 class="gold-type title">The Hollow Lanterns</h1>

  <div class="cover-art" role="img" aria-label="Photograph of the heroine in a dark laced jacket holding a fencing sword against a pale wall"></div>

  <p class="gold-type byline byline--first">by Marisol Devereux</p>
  <p class="gold-type byline byline--amp">&amp;</p>
  <p class="gold-type byline byline--second">Tobin Halvard</p>

  <p class="gold-type volume">VOL.1</p>
</main>
</body>
</html>
```